Private Chef booking platform landing page design

I need an amazing design for a landing page for my upcoming private chef booking platform Platerva. You can view my current page here: www.platerva.co.uk/mainindex.php. The design on this page is wrong right now. This platform is in Beta and the main purpose is to sign up chefs. Similar to what Rydexa.com is doing with their website -> become a driver. In my case we should have a button that says "become a chef", state the benefits of becoming a chef such as earning extra money, managing your time and bookings, increasing your client base and be creative with your food menus at the same time. Also, somewhere on the website it needs to say that we are currently in Beta mode and sign up to help us grow. In terms of visuals, I want the design to be sleek and clean and also adaptable to mobile devices as I am using html5. You can also re-design the current logo and choose any colours you think would be suitable for such a concept. Similar concept websites: hobwanderly.com and stovlin.com
Updates

Target Market(s)

upper middle class

Industry/Entity Type

Chef

Number of Pages Required

1 page

Font styles to use
Sans Serif

Requirements
Must have
• see brief and check hobwanderly.com and stovlin.com for inspiration and also rydexa.com
Nice to have
• see brief
Should not have
• bad visuals

```html
<!DOCTYPE html>
<html lang="en">
<head>
<meta charset="utf-8">
<title>Platerva – Private Chef Booking</title>
<link rel="stylesheet" href="https://fonts.googleapis.com/css2?family=Open+Sans:wght@400;600;700&family=Roboto+Condensed:wght@300;700&family=Roboto:wght@400;500&display=swap">
<style>
:root{
  --ink:#111111;
  --text:#3a3a3a;
  --muted:#555555;
  --accent:#f7a90f;
  --band:#eeeff1;
  --rule:#dddddd;
  --white:#ffffff;
  --footer:#000000;
}
*{margin:0;padding:0;box-sizing:border-box}
html,body{width:1200px;height:2242px;overflow:hidden;background:var(--white)}
body{position:relative;font-family:"Open Sans",Arial,sans-serif;color:var(--ink)}
.abs{position:absolute}
.center-x{transform:translateX(-50%);text-align:center;white-space:nowrap}

/* header */
.site-header{position:absolute;left:0;top:0;width:1200px;height:187px;background:var(--white)}
.brand{position:absolute;left:108px;top:68px;display:flex;align-items:center;gap:12px}
.brand-dot{width:30px;height:30px;border-radius:50%;background:var(--ink)}
.brand-name{font-family:"Roboto",sans-serif;font-size:34px;font-weight:500;color:var(--ink)}
.follow{position:absolute;left:862px;top:46px;font-family:"Roboto",sans-serif;font-size:12px;font-weight:500;color:var(--ink)}
.social-dot{position:absolute;top:47px;width:14px;height:14px;border-radius:50%}
.main-nav a{position:absolute;top:122px;font-family:"Roboto",sans-serif;font-size:13px;font-weight:500;color:var(--ink);text-decoration:none;white-space:nowrap}
.btn-signup,.btn-login{position:absolute;top:110px;height:40px;display:flex;align-items:center;justify-content:center;font-family:"Roboto",sans-serif;font-size:13px;font-weight:500}
.btn-signup{left:925px;width:82px;border:1.5px solid var(--ink);color:var(--ink)}
.btn-login{left:1017px;width:80px;background:var(--ink);color:var(--white)}

/* hero */
.hero{position:absolute;left:0;top:187px;width:1200px;height:684px;background:radial-gradient(ellipse at 50% 45%,#6a6a6a 0%,#3d3d3d 45%,#1e1e1e 100%)}
.hero-caption{position:absolute;left:414px;top:254px;width:373px;height:134px;background:rgba(20,20,20,.72);color:var(--white);font-family:"Roboto Condensed",sans-serif;font-weight:300;font-size:36px;line-height:47px;text-align:center;padding-top:20px}
.hero-cta{position:absolute;left:414px;top:390px;width:373px;height:70px;background:var(--accent);color:var(--white);font-family:"Roboto Condensed",sans-serif;font-weight:700;font-size:24px;display:flex;align-items:center;justify-content:center}
.hero-arrow{position:absolute;top:313px}
.dot{position:absolute;top:614px;width:21px;height:21px;border-radius:50%;background:var(--white)}
.dot.active{background:transparent;border:3px solid var(--white)}

/* section titles */
.section-title{position:absolute;left:600px;font-size:17px;font-weight:600;letter-spacing:2px;color:var(--ink)}
.section-title .hl{color:var(--accent)}
.title-rule{position:absolute;left:565px;width:70px;height:1px;background:var(--rule)}

/* how it works */
.step-num{position:absolute;top:1017px;width:34px;height:34px;border-radius:50%;background:var(--accent);color:var(--ink);font-size:14px;display:flex;align-items:center;justify-content:center;transform:translateX(-50%)}
.step-art{position:absolute;top:1083px;width:170px;height:157px;transform:translateX(-50%);background:linear-gradient(#f4f4f4,#e6e6e6)}
.step-title{position:absolute;top:1268px;font-size:14px;font-weight:700;line-height:20px;color:var(--ink)}
.step-text{position:absolute;top:1296px;font-size:13.5px;line-height:24px;color:var(--text)}
.step-divider{position:absolute;top:1020px;width:1px;height:344px;background:var(--rule)}

/* welcome */
.welcome{position:absolute;left:0;top:1418px;width:1200px;height:355px;background:var(--band)}
.welcome-text{position:absolute;left:169px;top:1542px;width:862px;font-size:13.4px;line-height:31px;color:var(--text);text-align:center}
.btn-more{position:absolute;left:547px;top:1693px;width:112px;height:36px;background:var(--ink);color:var(--white);font-size:12px;font-weight:700;display:flex;align-items:center;justify-content:center}

/* benefits */
.benefit-icon{position:absolute;top:1910px;width:52px;height:52px;border-radius:50%;background:var(--ink);display:flex;align-items:center;justify-content:center}
.benefit-label{position:absolute;top:1914px;font-size:14px;font-weight:700;line-height:23px;color:var(--ink)}

/* footer */
.site-footer{position:absolute;left:0;top:2014px;width:1200px;height:228px;background:var(--footer);color:var(--white)}
.footer-follow{position:absolute;left:600px;top:30px;font-family:"Roboto",sans-serif;font-size:12px}
.footer-dot{position:absolute;top:73px;width:14px;height:14px;border-radius:50%;background:var(--white)}
.footer-rule{position:absolute;left:332px;top:118px;width:538px;height:1px;background:#333}
.footer-links{position:absolute;left:600px;top:146px;font-family:"Roboto",sans-serif;font-size:12px}
.footer-copy{position:absolute;left:600px;top:180px;font-family:"Roboto",sans-serif;font-size:10.5px}
</style>
</head>
<body>

<header class="site-header">
  <div class="brand"><span class="brand-dot"></span><span class="brand-name">Platerva</span></div>
  <span class="follow">FOLLOW US ON</span>
  <span class="social-dot" style="left:967px;background:var(--ink)"></span>
  <span class="social-dot" style="left:1004px;background:#aaa"></span>
  <span class="social-dot" style="left:1042px;background:#aaa"></span>
  <span class="social-dot" style="left:1079px;background:#aaa"></span>
  <nav class="main-nav">
    <a style="left:414px">HOME</a>
    <a style="left:489px">ABOUT US</a>
    <a style="left:598px">HOW IT WORKS</a>
    <a style="left:736px">HELP</a>
    <a style="left:807px">CONTACT US</a>
  </nav>
  <div class="btn-signup">SIGNUP</div>
  <div class="btn-login">LOGIN</div>
</header>

<section class="hero" role="img" aria-label="Black and white photo of guests dining around a table served by a private chef">
  <svg class="hero-arrow" style="left:100px" width="34" height="42" viewBox="0 0 34 42"><path d="M26 4 L8 21 L26 38" fill="none" stroke="#fff" stroke-width="7"/></svg>
  <svg class="hero-arrow" style="left:1068px" width="34" height="42" viewBox="0 0 34 42"><path d="M8 4 L26 21 L8 38" fill="none" stroke="#fff" stroke-width="7"/></svg>
  <div class="hero-caption">Chefs made meals<br>in your home</div>
  <div class="hero-cta">BECOME A PRIVATE CHEF</div>
  <span class="dot" style="left:550px"></span>
  <span class="dot active" style="left:577px"></span>
  <span class="dot" style="left:604px"></span>
  <span class="dot" style="left:629px"></span>
</section>

<h2 class="section-title center-x" style="top:909px">HOW <span class="hl">IT</span> WORKS</h2>
<div class="title-rule" style="top:953px"></div>

<div class="step-num" style="left:202px">1</div>
<div class="step-num" style="left:475px">2</div>
<div class="step-num" style="left:743px">3</div>
<div class="step-num" style="left:1002px">4</div>
<div class="step-art" style="left:202px" role="img" aria-label="Sketch: a person booking a chef online"></div>
<div class="step-art" style="left:475px" role="img" aria-label="Sketch: chef cooking a delicious meal"></div>
<div class="step-art" style="left:743px" role="img" aria-label="Sketch: clean kitchen after the chef leaves"></div>
<div class="step-art" style="left:1002px" role="img" aria-label="Sketch: guests enjoying the party"></div>
<div class="step-divider" style="left:338px"></div>
<div class="step-divider" style="left:612px"></div>
<div class="step-divider" style="left:874px"></div>

<h3 class="step-title center-x" style="left:202px">I NEED A CHEF</h3>
<p class="step-text center-x" style="left:202px">Taciti lacus velit ante, non orci,<br>minus laoreet pede. Dui et eu,<br>aliquam penatibus.</p>
<h3 class="step-title center-x" style="left:475px;top:1268px">CHEF TAKE CARE<br>OF EVERYTHING</h3>
<p class="step-text center-x" style="left:475px;top:1316px">Taciti lacus velit ante, non orci,<br>minus laoreet pede</p>
<h3 class="step-title center-x" style="left:743px">CHEF COOK FOR YOU<br>AND YOUR GUESTS</h3>
<p class="step-text center-x" style="left:743px;top:1316px">Taciti lacus velit ante, non orci,<br>minus laoreet pede</p>
<h3 class="step-title center-x" style="left:1002px">YOU JUST ENJOY<br>THE PARTY</h3>
<p class="step-text center-x" style="left:1002px;top:1316px">Taciti lacus velit ante, non orci,<br>minus laoreet pede</p>

<section class="welcome"></section>
<h2 class="section-title center-x" style="top:1461px">WELCOME <span class="hl">TO</span> OUR SITE</h2>
<div class="title-rule" style="top:1503px"></div>
<p class="welcome-text">Contrary to popular belief, Lorem Ipsum is not simply random text. It has roots in a piece of classical Latin literature from 45 BC, making it over 2000 years old. Edmund Larrow, a Latin professor at Harwick-Dale College in Vermont, looked up one of the more obscure Latin words, consectetur, from a Lorem Ipsum passage, and going through the cites of the word in classical literature, discovered the undoubtable source. orem Ipsum comes from sections 1.10.32 and 1.10.33 of "de Finibus Bonorum et.</p>
<div class="btn-more">READ MORE</div>

<h2 class="section-title center-x" style="top:1813px"><span class="hl">OUR</span> BENEFITS</h2>
<div class="title-rule" style="top:1854px"></div>

<div class="benefit-icon" style="left:101px"><svg width="26" height="26" viewBox="0 0 26 26"><text x="13" y="15" font-family="Arial" font-weight="700" font-size="13" fill="#fff" text-anchor="middle">$</text><path d="M3 20 Q9 17 13 20 L22 18" fill="none" stroke="#fff" stroke-width="2"/></svg></div>
<div class="benefit-icon" style="left:322px"><svg width="22" height="22" viewBox="0 0 22 22"><rect x="2" y="4" width="18" height="16" fill="none" stroke="#fff" stroke-width="2"/><rect x="2" y="4" width="18" height="4" fill="#fff"/><rect x="6" y="11" width="3" height="3" fill="#fff"/><rect x="13" y="11" width="3" height="3" fill="#fff"/><rect x="6" y="15" width="3" height="3" fill="#fff"/></svg></div>
<div class="benefit-icon" style="left:622px"><svg width="22" height="22" viewBox="0 0 22 22"><path d="M2 3 H20 L11 12 Z" fill="#fff"/><rect x="10" y="11" width="2" height="7" fill="#fff"/><rect x="6" y="18" width="10" height="2" fill="#fff"/></svg></div>
<div class="benefit-icon" style="left:911px"><svg width="26" height="22" viewBox="0 0 26 22"><circle cx="13" cy="6" r="4" fill="#fff"/><circle cx="5" cy="8" r="3" fill="#fff"/><circle cx="21" cy="8" r="3" fill="#fff"/><path d="M6 20 Q13 8 20 20 Z" fill="#fff"/><path d="M0 19 Q5 11 9 16 L7 19Z M26 19 Q21 11 17 16 L19 19Z" fill="#fff"/></svg></div>

<div class="benefit-label" style="left:175px">EARN EXTRA<br>MONEY</div>
<div class="benefit-label" style="left:396px">FULLY MANAGE YOUR<br>BOOKINGS SCHEDULE</div>
<div class="benefit-label" style="left:698px">BE CREATIVE WITH<br>YOUR FOOD MENUS</div>
<div class="benefit-label" style="left:985px">EXPAND YOUR<br>CLIENTELE BASE</div>

<footer class="site-footer">
  <div class="footer-follow center-x">FOLLOW US ON</div>
  <span class="footer-dot" style="left:531px;background:var(--accent)"></span>
  <span class="footer-dot" style="left:567px"></span>
  <span class="footer-dot" style="left:604px"></span>
  <span class="footer-dot" style="left:641px"></span>
  <div class="footer-rule"></div>
  <div class="footer-links center-x">HOME &nbsp;| &nbsp;CONTACT US &nbsp;| &nbsp;ABOUT US &nbsp;| &nbsp;SIGN UP &nbsp;| &nbsp;LOGIN &nbsp;| &nbsp;HELP</div>
  <div class="footer-copy center-x">COPYRIGHTS @ 2015 ALL RIGHTS RESERVED</div>
</footer>

</body>
</html>
```